Pwrpt Describing Grant Attributes

We recently won a grant to deliver services to students with disabilities. I need a PowerPoint presentation to explain the grant to stakeholders. The PowerPoint should summarize the key attributes of the grant in a way that can be shared with anyone. I am attaching the entire Narrative, an abstract, a summary of the grant, and Measures that have to be obtained.

Target Market(s)

Educators

Requirements
Must have
• Use the Colors from our website: https://k7v.org/
Nice to have
• where can use https://portal.lrx.vendara.gov/ for any additional information

```html
<!DOCTYPE html>
<html lang="en">
<head>
<meta charset="utf-8">
<title>Stepway Futures – Grant Overview</title>
<link rel="stylesheet" href="https://fonts.googleapis.com/css2?family=Montserrat:wght@400;600;700;800&family=Open+Sans:wght@400;600&display=swap">
<style>
:root{
  --canvas:#ececec;
  --white:#ffffff;
  --blue:#1c5fb0;
  --blue-deep:#0f3f80;
  --navy:#12284a;
  --orange:#f28a22;
  --ink:#222b36;
  --text:#555d66;
  --pale:#eef3f9;
  --photo-a:#b9a592;
  --photo-b:#6f7d8d;
}
*{margin:0;padding:0;box-sizing:border-box}
html,body{width:1200px;height:3912px;overflow:hidden;background:var(--canvas)}
body{font-family:"Open Sans",Arial,sans-serif;color:var(--text);position:relative}
.slide{position:absolute;left:56px;width:1088px;height:612px;background:var(--white);overflow:hidden;box-shadow:0 2px 8px rgba(0,0,0,.12)}
.s1{top:20px}.s2{top:676px}.s3{top:1332px}.s4{top:1988px}.s5{top:2644px}.s6{top:3300px}
.photo{position:absolute;background:linear-gradient(135deg,var(--photo-a),var(--photo-b))}
.brand{position:absolute;display:flex;align-items:center;gap:10px;font-family:"Montserrat",Arial,sans-serif;font-weight:800;font-size:20px;color:var(--blue);letter-spacing:.5px;text-transform:uppercase}
.brand .dot{width:26px;height:26px;border-radius:50%;background:var(--orange)}
.header{position:absolute;left:0;top:0;width:100%;height:100px;display:flex;align-items:center;padding-left:34px}
.header .brand{position:static}
.header .rule{width:3px;height:56px;background:var(--orange);margin:0 26px}
.title{font-family:"Montserrat",Arial,sans-serif;font-weight:800;color:var(--ink);font-size:26px;text-transform:uppercase;line-height:1.15}
/* slide 1 */
.s1 .photo{inset:0;background:linear-gradient(120deg,#c7b5a2,#8c8f95 55%,#5d6b7b)}
.s1 .brandbox{position:absolute;left:22px;top:22px;background:var(--white);padding:16px 22px}
.s1 .brandbox .brand{position:static}
.s1 .hero{position:absolute;left:0;bottom:0;width:100%;height:190px;background:linear-gradient(90deg,rgba(10,20,40,.85),rgba(10,20,40,.2));padding:60px 0 0 36px;color:var(--white)}
.s1 h1{font-family:"Montserrat",Arial,sans-serif;font-weight:800;font-size:46px}
.s1 .hero p{font-size:19px;margin-top:8px}
/* slide 2 */
.s2 .photo{left:0;top:100px;width:560px;height:512px}
.s2 .body{position:absolute;left:610px;top:200px;width:440px;font-size:13.5px;line-height:1.6}
/* slide 3 */
.s3 .panel{position:absolute;left:0;top:100px;width:560px;height:512px;background:linear-gradient(160deg,var(--blue),var(--blue-deep));padding:28px 34px;color:var(--white)}
.s3 .photo{left:560px;top:100px;width:528px;height:512px}
.bullets{list-style:none}
.bullets li{position:relative;padding-left:18px;font-size:12.5px;line-height:1.45;margin-bottom:11px}
.bullets li::before{content:"";position:absolute;left:0;top:6px;width:7px;height:7px;border-radius:50%;background:var(--orange)}
/* slide 4 */
.s4 .left{position:absolute;left:0;top:0;width:440px;height:612px;background:var(--pale)}
.s4 .brand{left:34px;top:36px}
.s4 .photo{left:-90px;top:150px;width:520px;height:520px;border-radius:50%;border:10px solid var(--white)}
.s4 .heading{position:absolute;left:480px;top:34px;display:flex;align-items:stretch}
.s4 .heading .rule{width:3px;background:var(--orange);margin-right:20px}
.s4 .intro{position:absolute;left:480px;top:130px;width:570px;font-size:12.5px;line-height:1.55}
.s4 .box{position:absolute;left:480px;top:290px;width:570px;height:290px;background:var(--blue);padding:26px 28px;color:var(--white)}
/* slide 5 */
.s5 .header .title{font-size:19px;max-width:620px}
.s5 .intro{position:absolute;left:34px;top:124px;width:560px;font-size:12.5px;line-height:1.55}
.s5 .list{position:absolute;left:34px;top:290px;list-style:none}
.s5 .list li{display:flex;align-items:center;gap:12px;font-size:14px;color:var(--ink);height:36px}
.s5 .list li::before{content:"";width:12px;height:12px;background:var(--orange)}
.s5 .photo{left:640px;top:110px;width:448px;height:502px}
/* slide 6 */
.s6{background:linear-gradient(150deg,var(--blue),var(--blue-deep))}
.s6 .brand{left:50%;top:190px;transform:translateX(-50%);color:var(--white);font-size:34px;gap:16px}
.s6 .brand .dot{width:40px;height:40px}
.s6 .thanks{position:absolute;left:0;width:100%;top:330px;text-align:center;color:var(--white);font-family:"Montserrat",Arial,sans-serif;font-weight:700;font-size:52px;letter-spacing:4px}
.s6 .line{position:absolute;left:294px;width:500px;height:2px;background:rgba(255,255,255,.7)}
</style>
</head>
<body>

<section class="slide s1">
  <div class="photo" role="img" aria-label="Photo of a teacher leading an engaged classroom of students"></div>
  <div class="brandbox"><div class="brand"><span class="dot"></span>Stepway Futures</div></div>
  <div class="hero">
    <h1>We're SWF.</h1>
    <p>When education becomes relevant, learners fully engage.</p>
  </div>
</section>

<section class="slide s2">
  <div class="header"><div class="brand"><span class="dot"></span>Stepway Futures</div><span class="rule"></span><h2 class="title">Magnitude of the Need</h2></div>
  <div class="photo" role="img" aria-label="Photo of two students working together at a computer"></div>
  <p class="body">Two major trends in education today are increasingly influencing school priorities and programs. The first is attention through a career lens. Schools need to increase their focus on preparing students for postsecondary education options and for work. The second is partnerships. Schools cannot accomplish many of its initiatives for improving student outcomes, particularly in special education, without multi-sector public and private partnerships, resources, and support. Bringing schools and community partners together can produce cooperative career-focused programs that align the realities of the workplace with what students learn in school. When applied to special education, we need "all hands on deck."</p>
</section>

<section class="slide s3">
  <div class="header"><div class="brand"><span class="dot"></span>Stepway Futures</div><span class="rule"></span><h2 class="title">Project Objectives and Outcomes</h2></div>
  <div class="panel">
    <ul class="bullets">
      <li>Relevant CCL Content: Aligning course material with the workforce requirements in New Mexico.</li>
      <li>Enhanced Access to Career Exploration: Ensuring that students with disabilities have access and tools that facilitate career exploration, aiding their transition from school.</li>
      <li>Improved Math Proficiency and Motivation: Enhancing students' mathematical skills and motivation levels to better prepare them for an evolving job market.</li>
      <li>Fostering Self-Awareness and Advocacy: Empowering students with disabilities to build self-confidence and advocate for themselves effectively across their needs.</li>
      <li>Enhancing Teacher and Partner Training: Equipping K-12 teachers and partners with the knowledge and skills to support the career pursuits of students with disabilities.</li>
      <li>Building a Unified Vision: Demonstrating the power of a shared vision (CCL) to connect educators, businesses, community stakeholders, and parents, with improved approaches to align resources and service delivery models for students with disabilities.</li>
    </ul>
  </div>
  <div class="photo" role="img" aria-label="Photo of a student concentrating while writing at a desk"></div>
</section>

<section class="slide s4">
  <div class="left">
    <div class="brand"><span class="dot"></span>Stepway Futures</div>
    <div class="photo" role="img" aria-label="Circular photo of a smiling teacher holding a folder in a school hallway"></div>
  </div>
  <div class="heading"><span class="rule"></span><h2 class="title">A.1.1 Challenges to<br>Equitable Access</h2></div>
  <p class="intro">Schools face many challenges to ensuring equitable access for students with disabilities. Some of these challenges include inadequate program design and accommodations to help students with disabilities participate, lack of appropriate career and work-based learning, the need for specialized, ongoing training for teachers and community partners working with this population, and identification of business mentors who can help prepare these students for work by sharing what they do at work.</p>
  <div class="box">
    <ul class="bullets">
      <li>The proposed CCL digital curricula Career Exploration and Stepway Futures in Math, an internally recognized CCL curricula used in multiple states.</li>
      <li>Teacher shortages across the state (and the nation) are particularly hard felt in rural regions of New Mexico, which makes up roughly one third of the population of the state.</li>
      <li>A recent NMED report notes that the lack of communication and sharing between schools, employers, and training institutions contributes to the deficiency of student preparation for the changing needs of the workforce (NMED, 2023).</li>
      <li>The State of New Mexico has challenges to equitable access across the many remote rural regions in the state.</li>
    </ul>
  </div>
</section>

<section class="slide s5">
  <div class="header"><div class="brand"><span class="dot"></span>Stepway Futures</div><span class="rule"></span><h2 class="title">Innovation to Support Students with Disabilities in Career-Connected Learning(CCLINNM)</h2></div>
  <p class="intro">SWF will revolutionize how students with disabilities engage with and benefit from career-connected learning. The federal grant, Career Connected Learning in New Mexico (CCLINNM) represents a significant departure from traditional education models by customizing career exploration, skill development, and transition planning to cater specifically to the unique needs of students with disabilities. Here is a detailed description of the innovative components that will be created to support this model:</p>
  <ul class="list">
    <li>Adaptive Digital Curriculum</li>
    <li>Mentorship and Career Exploration</li>
    <li>Inclusive Career Exploration Tools</li>
    <li>Specialized Math Curriculum</li>
    <li>Career Page and Self-Advocacy Tools</li>
    <li>Teacher and Partner Training</li>
    <li>Comprehensive Data Collection and Analysis</li>
    <li>Longitudinal Monitoring</li>
  </ul>
  <div class="photo" role="img" aria-label="Photo of a teacher presenting at a whiteboard"></div>
</section>

<section class="slide s6">
  <div class="brand"><span class="dot"></span>Stepway Futures</div>
  <span class="line" style="top:310px"></span>
  <p class="thanks">THANK YOU</p>
  <span class="line" style="top:405px"></span>
</section>

</body>
</html>
```